Wealth Education Business Needs Sharp Business Card Design

We need a business card design for a recently launched investor education business called Harbor Crest.

The final design should promote security, empowerment, self improvement and financial gain. The card will ideally promote the stature of the business.

For more information and colours please visit harborcrest.com.au

Target Market(s)

Corporate executives and high net worth individuals

Industry/Entity Type

Education

Contact Information for Business Card

Name
Position
Contact Address
Phone
Mobile
Email
Website

```html
<!DOCTYPE html>
<html lang="en">
<head>
<meta charset="utf-8">
<title>Harbor Crest Business Card</title>
<link href="https://fonts.googleapis.com/css2?family=Michroma&display=swap" rel="stylesheet">
<style>
  :root {
    --bg: #8a8d8f;
    --paper: #ffffff;
    --charcoal: #3f3b3b;
    --teal: #0f6f6c;
    --ink: #2f2c2c;
    --light: #f4f4f4;
    --accent: #2aa3c6;
  }
  * { box-sizing: border-box; margin: 0; padding: 0; }
  html, body { width: 1200px; height: 771px; overflow: hidden; }
  body {
    background: var(--bg);
    font-family: "Michroma", sans-serif;
    display: flex;
    align-items: center;
    justify-content: center;
    gap: 40px;
  }
  .card {
    position: relative;
    width: 540px;
    height: 309px;
    background: var(--paper);
    box-shadow: 0 6px 18px rgba(0,0,0,0.25);
    overflow: hidden;
  }
  .card-art { position: absolute; inset: 0; }
  .contact-block {
    position: absolute;
    left: 34px;
    top: 34px;
    color: var(--light);
  }
  .person-name { font-size: 15px; letter-spacing: 1px; text-transform: uppercase; }
  .person-role { font-size: 10px; margin-top: 4px; }
  .address { font-size: 10px; line-height: 1.7; margin-top: 22px; }
  .contact-list { list-style: none; margin-top: 14px; font-size: 9.5px; }
  .contact-list li { display: flex; align-items: center; gap: 8px; height: 19px; }
  .contact-list svg { width: 12px; height: 12px; flex: none; }
  .brand {
    position: absolute;
    display: flex;
    align-items: center;
    gap: 12px;
    color: var(--ink);
  }
  .brand-dot { border-radius: 50%; background: var(--accent); flex: none; }
  .brand-name { letter-spacing: 3px; text-transform: uppercase; white-space: nowrap; }
  .card-front .brand {
    right: 22px;
    top: 176px;
    flex-direction: column;
    align-items: flex-end;
    gap: 10px;
  }
  .card-front .brand-dot { width: 22px; height: 22px; margin-right: 14px; }
  .card-front .brand-name { font-size: 12px; letter-spacing: 2px; }
  .card-back .brand { left: 50%; top: 50%; transform: translate(-50%, -50%); flex-direction: column; gap: 18px; }
  .card-back .brand-dot { width: 44px; height: 44px; }
  .card-back .brand-name { font-size: 24px; }
</style>
</head>
<body>
  <section class="card card-front">
    <svg class="card-art" viewBox="0 0 540 309" aria-hidden="true">
      <path d="M412 0 H452 C390 70 332 170 302 309 H290 C312 190 350 90 412 0 Z" fill="var(--teal)"/>
      <path d="M0 0 H400 C335 90 298 200 286 309 H0 Z" fill="var(--charcoal)"/>
    </svg>
    <div class="contact-block">
      <p class="person-name">Marcus Bennett</p>
      <p class="person-role">Managing Director</p>
      <p class="address">12 Level 9 Quay,<br>Harbour Road NSW</p>
      <ul class="contact-list">
        <li>
          <svg viewBox="0 0 12 12"><path d="M2 1 L4.5 1 L5.5 3.5 L4 4.5 C4.7 6 6 7.3 7.5 8 L8.5 6.5 L11 7.5 L11 10 C6 11 1 6 2 1 Z" fill="var(--light)"/></svg>
          012 555 0147
        </li>
        <li>
          <svg viewBox="0 0 12 12"><rect x="3" y="0.5" width="6" height="11" rx="1" fill="none" stroke="var(--light)"/><circle cx="6" cy="9.5" r="0.7" fill="var(--light)"/></svg>
          012 555 0148
        </li>
        <li>
          <svg viewBox="0 0 12 12"><rect x="0.5" y="2.5" width="11" height="7" fill="none" stroke="var(--light)"/><path d="M0.5 2.5 L6 7 L11.5 2.5" fill="none" stroke="var(--light)"/></svg>
          mbennett@harborcrest.com.au
        </li>
        <li>
          <svg viewBox="0 0 12 12"><circle cx="6" cy="6" r="5.3" fill="none" stroke="var(--light)"/><ellipse cx="6" cy="6" rx="2.3" ry="5.3" fill="none" stroke="var(--light)"/><path d="M0.7 6 H11.3" stroke="var(--light)"/></svg>
          www.harborcrest.com.au
        </li>
      </ul>
    </div>
    <div class="brand">
      <span class="brand-dot"></span>
      <span class="brand-name">Harbor Crest</span>
    </div>
  </section>

  <section class="card card-back">
    <div class="brand">
      <span class="brand-dot"></span>
      <span class="brand-name">Harbor Crest</span>
    </div>
  </section>
</body>
</html>
```